AN ELEGANT COSMETIC LABLE THAT CAN EASILY BE ALTERED TO FIT A VARIETY OF DIFFERENT PRODUCTS.

Predictable and ordinary designs are NOT welcome. Creative minds wanted.

Looking for a professional lable that is Canadian/USA Standard and compliant with the Food and Drug - Cosmetic Act in Onatrio. Which has a clean and elegant look, with a hint of holistic vibes.

This lable should be sleak and flexible to be altered to fit a variety of different products. Let your creativity come out with this project, the crazy and unpredictable are welcome.

This lable may be on the next biggest Cosmetic brand in the world. If you can see it, you can design it. All the best, looking forward to working with you.

Target Market(s)

Everyone who is looking for a clean natural lifestyle. The elite crowd.

Industry/Entity Type

Cosmetics

Font styles to use
Serif
Script

Colors

Designer to choose only greyscale colors for use in the design.

Requirements
Must have
• Company Name " BRELLOW'S" and or Logo. See attachment
Nice to have
• One or more solid bars that can be colored to match the main product ingredient colour.
Should not have
• Too much different colors or images

```html
<!DOCTYPE html>
<html lang="en">
<head>
<meta charset="utf-8">
<title>Brellow's Aloe Vera Label</title>
<link href="https://fonts.googleapis.com/css2?family=Kurale&family=Yellowtail&family=Cinzel:wght@400&display=swap" rel="stylesheet">
<style>
  :root {
    --ink: #ffffff;
    --ink-soft: #d9d9d9;
    --bg-deep: #050805;
    --bg-mid: #111811;
    --leaf-light: #7fcf4a;
    --leaf-mid: #3f8f2a;
    --leaf-dark: #123a14;
    --icon-line: #e8e8e8;
  }
  html, body { margin: 0; padding: 0; overflow: hidden; }
  body { width: 1200px; height: 557px; background: var(--bg-deep); }
  .label {
    position: relative; width: 1200px; height: 557px; overflow: hidden;
    background: radial-gradient(ellipse at 50% 45%, #1c2a1a 0%, var(--bg-mid) 40%, var(--bg-deep) 85%);
    font-family: "Kurale", Georgia, serif; color: var(--ink);
  }
  .plant-photo {
    position: absolute; left: 270px; top: 120px; width: 580px; height: 437px;
    background:
      radial-gradient(ellipse at 50% 75%, var(--leaf-light) 0%, var(--leaf-mid) 30%, var(--leaf-dark) 60%, transparent 78%);
    opacity: .85;
  }
  .brand {
    position: absolute; left: 0; width: 1200px; top: 14px; text-align: center;
    font-size: 44px; letter-spacing: 6px; line-height: 1; color: var(--ink);
  }
  .block { position: absolute; }
  .block h2 { margin: 0; font-weight: 400; font-size: 20px; line-height: 1; }
  .block p { margin: 0; font-size: 15px; line-height: 18.5px; }
  .left { left: 39px; width: 350px; }
  .left p { margin-top: 11px; }
  .right { left: 834px; width: 340px; }
  .right h2 { font-size: 19px; }
  .right p { font-size: 13.2px; line-height: 15.6px; margin-top: 9px; }

  .product { position: absolute; left: 0; width: 1200px; text-align: center; }
  .product-type { top: 380px; font-size: 26px; color: #f3f3e8; }
  .product-name { font-family: "Yellowtail", cursive; line-height: 1; text-shadow: 0 0 8px rgba(0,0,0,.4); }
  .name-primary { top: 408px; font-size: 64px; }
  .name-secondary { top: 468px; font-size: 52px; }
  .net-weight { top: 526px; font-size: 17px; letter-spacing: 3px; }

  .claims { position: absolute; left: 832px; display: flex; gap: 15px; }
  .claim { width: 58px; text-align: center; font-size: 14.5px; line-height: 17px; }
  .claim svg { display: block; margin: 0 auto 8px; }
  .claims-en { top: 170px; }
  .claims-fr { top: 423px; gap: 17px; }
  .claims-fr .claim { font-size: 15px; line-height: 18px; }
  .claim .muted { color: #bdbdbd; }
</style>
</head>
<body>
<div class="label">
  <div class="plant-photo" role="img" aria-label="Aloe vera plant with dew-covered leaves glowing green"></div>

  <div class="brand">BRELLOW'S</div>

  <section class="block left" style="top:34px">
    <h2>Ingredients:</h2>
    <p>Aloe gel, coconut oil, water, cetearyl alcohol, glycerin, sunflower oil, shea butter, glycerin stearate, beeswax, dimethicon, phenoxyethanol, sodium polyacrylate, vitamin E.</p>
  </section>
  <section class="block left" style="top:175px">
    <h2>Ingrédients :</h2>
    <p>Gel d'aloès, huile de noix de coco, eau, alcool cetearyl, glycérine, huile de tournesol, beurre de karité, stéarate de glycérine, cire d'abeille, diméthicone, phénoxyethanol, polyacrylate de sodium, vitamine E.</p>
  </section>
  <section class="block left" style="top:331px; width:370px">
    <h2>Warning:</h2>
    <p>This product is not intended for human consumption. If irritation occurs, discontinue use.</p>
  </section>
  <section class="block left" style="top:434px; width:250px">
    <h2>Attention:</h2>
    <p>Ce produit n'est pas destiné à la consommation humaine. En cas d'irritation, cesser l'utilisation</p>
  </section>

  <section class="block right" style="top:34px">
    <h2>Details:</h2>
    <p>Luxuriously rich moisturizer that melts effortlessly into the skin, leaving it soft and luminous. This new and improved formulation is pH-optimized for glowing skin that remains hydrated and protected all day long. It leaves no sticky residues and is easy to spread while still maintaining the look and feel of a premium product.</p>
  </section>

  <div class="claims claims-en">
    <div class="claim"><svg width="57" height="57" viewBox="0 0 57 57" fill="none" stroke="var(--icon-line)" stroke-width="2"><circle cx="28.5" cy="28.5" r="27"/><circle cx="28" cy="33" r="10"/><rect x="24" y="19" width="8" height="5"/><line x1="9" y1="48" x2="48" y2="9"/></svg>Fragrance<br>FREE</div>
    <div class="claim"><svg width="57" height="57" viewBox="0 0 57 57" fill="none" stroke="var(--icon-line)" stroke-width="2"><circle cx="28.5" cy="28.5" r="27"/><line x1="28.5" y1="12" x2="28.5" y2="46"/><ellipse cx="23" cy="22" rx="3" ry="5"/><ellipse cx="34" cy="22" rx="3" ry="5"/><ellipse cx="23" cy="33" rx="3" ry="5"/><ellipse cx="34" cy="33" rx="3" ry="5"/><line x1="9" y1="48" x2="48" y2="9"/></svg>Gluten<br>FREE</div>
    <div class="claim" style="width:70px"><svg width="57" height="57" viewBox="0 0 57 57" fill="none" stroke="var(--icon-line)" stroke-width="2"><circle cx="28.5" cy="28.5" r="27"/><path d="M28.5 12 C20 24 18 30 18 35 a10.5 10.5 0 0 0 21 0 c0-5-2-11-10.5-23z"/><line x1="9" y1="48" x2="48" y2="9"/></svg>Phthalate<br>FREE</div>
    <div class="claim"><svg width="57" height="57" viewBox="0 0 57 57" fill="none" stroke="var(--icon-line)" stroke-width="2"><circle cx="28.5" cy="28.5" r="27"/><ellipse cx="22" cy="18" rx="4" ry="8"/><ellipse cx="33" cy="18" rx="4" ry="8"/><ellipse cx="28" cy="36" rx="11" ry="9"/><line x1="9" y1="48" x2="48" y2="9"/></svg>Cruelty<br>FREE</div>
  </div>

  <section class="block right" style="top:281px">
    <h2>Détails:</h2>
    <p style="margin-top:8px">Hydratant riche et luxueux qui fond sans effort dans la peau, la laissant douce et lumineuse. Cette nouvelle formulation améliorée a un pH optimisé pour une peau éclatante qui reste hydratée et protégée toute la journée. Il ne laisse aucun résidu collant et est facile à étaler tout en conservant l'apparence et la sensation d'un produit haut de gamme.</p>
  </section>

  <div class="claims claims-fr">
    <div class="claim"><svg width="59" height="59" viewBox="0 0 57 57" fill="none" stroke="var(--icon-line)" stroke-width="2"><circle cx="28.5" cy="28.5" r="27"/><circle cx="28" cy="33" r="10"/><rect x="24" y="19" width="8" height="5"/><line x1="9" y1="48" x2="48" y2="9"/></svg><span class="muted">Sans<br>parfum</span></div>
    <div class="claim"><svg width="59" height="59" viewBox="0 0 57 57" fill="none" stroke="var(--icon-line)" stroke-width="2"><circle cx="28.5" cy="28.5" r="27"/><line x1="28.5" y1="12" x2="28.5" y2="46"/><ellipse cx="23" cy="22" rx="3" ry="5"/><ellipse cx="34" cy="22" rx="3" ry="5"/><ellipse cx="23" cy="33" rx="3" ry="5"/><ellipse cx="34" cy="33" rx="3" ry="5"/><line x1="9" y1="48" x2="48" y2="9"/></svg>Sans<br>gluten</div>
    <div class="claim" style="width:64px"><svg width="59" height="59" viewBox="0 0 57 57" fill="none" stroke="var(--icon-line)" stroke-width="2"><circle cx="28.5" cy="28.5" r="27"/><path d="M28.5 12 C20 24 18 30 18 35 a10.5 10.5 0 0 0 21 0 c0-5-2-11-10.5-23z"/><line x1="9" y1="48" x2="48" y2="9"/></svg>Sans<br>phtalate</div>
    <div class="claim"><svg width="59" height="59" viewBox="0 0 57 57" fill="none" stroke="var(--icon-line)" stroke-width="2"><circle cx="28.5" cy="28.5" r="27"/><ellipse cx="22" cy="18" rx="4" ry="8"/><ellipse cx="33" cy="18" rx="4" ry="8"/><ellipse cx="28" cy="36" rx="11" ry="9"/><line x1="9" y1="48" x2="48" y2="9"/></svg>Cruelty<br>FREE</div>
  </div>

  <div class="product product-type">ALOE VERA</div>
  <div class="product product-name name-primary">Skin Drencher</div>
  <div class="product product-name name-secondary">Pean Drencher</div>
  <div class="product net-weight">453.59 g/16 oz</div>
</div>
</body>
</html>
```